BRELM - Letterhead

Willowmere Institute of Letters and Crafts (BRELM) is a non-profit organization that operates two tuition-free public schools - BRELM Elementary for grades K to 5th and BRELM College Prep for grades 6-12.

We are looking for a letterhead primarily to be used on Google Docs and Microsoft Word. Attached are two versions of our logo. One with our name spelled out and one with the acronym.

For Letterhead, we would like 3 addresses listed:

BRELM HQ
41872 Hollow Brook Lane, Suite 308
Laguna Niguel, CA 92677

BRELM Elementary (K-5)
18460 Marsh Ridge Boulevard
Laguna Niguel, CA 92677

BRELM College Prep (6-12)
27314 Del Sol Terrace
San Juan Capistrano, CA 92675

Our Phone Number is (555) 418-7062
Our Fax Number is the same (555) 418-7062

Our website is www.brelmschools.org

Target Market(s)

Education

Industry/Entity Type

Education

Font styles to use
Sans Serif

Colors
0054AA
0677BA
7BADD7
CADEEF
E8F1F8

Requirements
Must have
• Logo, Address, Phone Number, Website.
Nice to have
• Modern and clean design.
Should not have
• Prefer that there is no bleed -- the letterhead will mostly be used in PDF format however sometimes it will be printed and our printers can not do a full bleed

```html
<!DOCTYPE html>
<html lang="en">
<head>
<meta charset="utf-8">
<title>BRELM Letterhead</title>
<link href="https://fonts.googleapis.com/css2?family=Inter:wght@400;500;600&family=Arimo:wght@400&display=swap" rel="stylesheet">
<style>
  :root {
    --backdrop: #e4ddd4;
    --paper: #f4f4f5;
    --brand-blue: #0d3da0;
    --ink: #3c3c3e;
    --ink-soft: #4a4a4c;
    --rule: #55555a;
    --band-red: #e9543a;
    --band-yellow: #e2b812;
    --band-green: #168f3b;
    --band-sky: #0a7dc2;
    --band-navy: #0b3ea3;
    --signature-tone: #e6e6e8;
  }
  * { box-sizing: border-box; margin: 0; padding: 0; }
  html, body { width: 1200px; height: 1141px; overflow: hidden; }
  body { background: var(--backdrop); position: relative; }

  .letterhead {
    position: absolute; left: 208px; top: 20px;
    width: 784px; height: 1100px;
    background: var(--paper);
    box-shadow: 0 2px 8px rgba(0,0,0,0.12);
  }
  .color-spine {
    position: absolute; left: 0; top: 0; width: 10px; height: 100%;
    display: flex; flex-direction: column;
  }
  .color-spine span { flex: 1; }
  .color-spine .red { background: var(--band-red); }
  .color-spine .yellow { background: var(--band-yellow); }
  .color-spine .green { background: var(--band-green); }
  .color-spine .sky { background: var(--band-sky); }
  .color-spine .navy { background: var(--band-navy); }

  .brand {
    position: absolute; left: 58px; top: 114px;
    display: flex; align-items: center; gap: 7px;
    font-family: "Inter", sans-serif; font-weight: 500;
    font-size: 24px; color: var(--brand-blue); letter-spacing: 0.3px;
  }
  .brand-square { width: 14px; height: 14px; background: var(--brand-blue); }

  .campus-list {
    position: absolute; top: 113px; left: 187px;
    display: flex;
    font-family: "Inter", sans-serif; font-size: 10px; line-height: 13.3px;
    color: var(--ink);
  }
  .campus { padding-right: 13px; }
  .campus + .campus { border-left: 1px solid var(--rule); padding-left: 13px; }
  .campus-name { color: var(--brand-blue); font-weight: 600; }

  .letter {
    position: absolute; left: 59px; top: 274px; width: 667px;
    font-family: "Arimo", sans-serif; color: var(--ink-soft);
  }
  .salutation { font-size: 18.5px; margin-bottom: 32px; color: var(--ink); }
  .letter p {
    font-size: 11px; line-height: 16.6px; text-align: justify;
    margin-bottom: 17px;
  }
  .letter p.closing { margin-top: 33px; margin-bottom: 18px; }
  .signature {
    width: 225px; height: 64px; background: var(--signature-tone);
    border-radius: 3px;
  }

  .contact-bar {
    position: absolute; top: 1040px; left: 0; width: 100%;
    display: flex; justify-content: center; align-items: center; gap: 14px;
    font-family: "Inter", sans-serif; font-size: 13px; color: var(--ink);
    padding-left: 10px;
  }
  .contact-item { display: flex; align-items: center; gap: 8px; }
  .contact-item svg { width: 10px; height: 10px; fill: var(--brand-blue); }
</style>
</head>
<body>
  <main class="letterhead">
    <div class="color-spine">
      <span class="red"></span><span class="yellow"></span><span class="green"></span><span class="sky"></span><span class="navy"></span>
    </div>

    <div class="brand"><span class="brand-square"></span>BRELM</div>

    <div class="campus-list">
      <div class="campus">
        <div class="campus-name">BRELM HQ</div>
        <div>41872 Hollow Brook Lane, Suite</div>
        <div>308, Laguna Niguel, CA 92677</div>
      </div>
      <div class="campus">
        <div class="campus-name">BRELM Elementary (K-5)</div>
        <div>18460 Marsh Ridge Boulevard</div>
        <div>Laguna Niguel, CA 92677</div>
      </div>
      <div class="campus">
        <div class="campus-name">BRELM College Prep (6-12)</div>
        <div>27314 Del Sol Terrace</div>
        <div>San Juan Capistrano, CA 92675</div>
      </div>
    </div>

    <article class="letter">
      <div class="salutation">Dear Mr. Alder,</div>
      <p>Lorem ipsum dolor sit amet, consectetur adipiscing elit. Donec orci purus, luctus vitae dignissim eu, iaculis sed purus. Vivamus faucibus, ipsum nec aliquet viverra, leo mauris condimentum ligula, sit amet sagittis enim ligula quis arcu. Nam egestas tortor id nisi porttitor mattis. In tortor ante, ultricies in suscipit a, tempus non massa. Vivamus et auctor mi. Fusce vel massa nulla. Phasellus nec eros mauris, et scelerisque orci.</p>
      <p>Donec malesuada orci vitae nulla accumsan porta a id massa. Quisque accumsan iaculis magna sit amet fringilla. Maecenas consequat, magna eget tincidunt semper, odio nibh rutrum mi, id feugiat ante nisi eu risus. Vestibulum nunc orci, rhoncus a placerat in, ultricies in mi. Cras mattis varius eros, vel fringilla nisi suscipit eget. Quisque scelerisque sagittis nulla at porttitor.</p>
      <p>Sed id augue vitae urna euismod commodo aliquet a quam. Pellentesque arcu velit, cursus et malesuada ut, consequat et diam. Nullam erat sem, rhoncus id ullamcorper vitae, rhoncus et arcu. In ultricies ultricies nulla, ut rutrum nisi iaculis at. Donec eu magna a metus ornare faucibus. Fusce aliquet faucibus ultricies. Morbi semper, est id tincidunt gravida, sem arcu adipiscing lacus, ac bibendum nulla leo eu purus. Quisque nec diam sed risus consectetur a ccumsan quis quis nibh. Vestibulum id purus lorem.</p>
      <p>It is a long established fact that a reader will be distracted by the readable content of a page when looking at its layout. The point of using Lorem Ipsum is that it has a more-or-less normal distribution of letters, as opposed to using 'Content here, content here', making it look like readable English. Many desktop publishing packages</p>
      <p>ada ut, consequat et diam. Nullam erat sem, rhoncus id ullamcorper vitae, rhoncus et arcu. In ultricies ultricies nulla, ut rutrum nisi iaculis at. Donec eu magna a metus ornare faucibus. Fusce aliquet faucibus ultricies. Morbi semper,</p>
      <p class="closing">Sincerely,</p>
      <div class="signature" role="img" aria-label="Handwritten signature of the sender"></div>
    </article>

    <footer class="contact-bar">
      <span class="contact-item">
        <svg viewBox="0 0 24 24" aria-hidden="true"><path d="M6.6 10.8a15.1 15.1 0 0 0 6.6 6.6l2.2-2.2c.3-.3.7-.4 1-.2 1.1.4 2.3.6 3.6.6.6 0 1 .4 1 1V20c0 .6-.4 1-1 1A17 17 0 0 1 3 4c0-.6.4-1 1-1h3.5c.6 0 1 .4 1 1 0 1.3.2 2.5.6 3.6.1.3 0 .7-.2 1z"/></svg>
        (555) 418-7062
      </span>
      <span class="contact-item">
        <svg viewBox="0 0 24 24" aria-hidden="true"><path d="M2 5h20v14H2z M2 5l10 8 10-8" fill="var(--brand-blue)"/><path d="M3 6l9 7 9-7" fill="none" stroke="#f4f4f5" stroke-width="2"/></svg>
        (555) 418-7062
      </span>
      <span class="contact-item">
        <svg viewBox="0 0 24 24" aria-hidden="true"><g fill="none" stroke="var(--brand-blue)" stroke-width="2"><circle cx="12" cy="12" r="10"/><ellipse cx="12" cy="12" rx="4" ry="10"/><path d="M2 12h20M4 7h16M4 17h16"/></g></svg>
        www.brelmschools.org
      </span>
    </footer>
  </main>
</body>
</html>
```